Roofing Company needs YOU to help put us on top!

Brightpeak Roofing, a fresh new company with quality and Innovation in mind, needs your help to stand out in the competitive Chicago market. With over 30 years of experience, all the right people and tools for the job, the only thing we are missing is your creative ideas in web design to help us grow our online presence.
Our Company offers exceptional quality at reasonable prices, we work for the everyday people both blue collar and white collar.

We have used Craftswarm in the past with multiple successful campaigns, we are excited to see what you can come up with for our website.

www.BrightpeakRoofing.example will be the domain

We will be hiring a photographer for visual content on our pages later. Stock photos are okay to use but should follow theme.

Thank you for taking the time on the submissions, if you have any questions don't hesitate to ask and we will provide whatever is needed to you.

Target Market(s)

Homeowners & Commercial Clients between 21-65

Industry/Entity Type

Roofing

Coding

Coded - Design and coding required

Number of Pages Required

4 page

Font styles to use
Sans Serif

Colors
ffffff
ec1f27
000000
5c5c5c
757575
b2b2b2

Requirements
Must have
• Color Scheme - should follow around our logo
• As for pages we were looking for an About, Services, Projects (gallery page) and Contact.
• Main page please include social media links and a a place so people could use tillbee to make payments
• Website should work on desktop as well as mobile platforms
Nice to have
• A Live chat feature would be nice if possible
Should not have
• Obscure Colors or Common web templates

```html
<!DOCTYPE html>
<html lang="en">
<head>
<meta charset="utf-8">
<title>Brightpeak Roofing</title>
<link href="https://fonts.googleapis.com/css2?family=Open+Sans:wght@400;600;700;800&display=swap" rel="stylesheet">
<style>
:root{
  --red:#ec1f27;
  --black:#000000;
  --dark:#2b2b2b;
  --charcoal:#3a3a3a;
  --grey:#5c5c5c;
  --mid:#757575;
  --light:#b2b2b2;
  --white:#ffffff;
}
*{margin:0;padding:0;box-sizing:border-box}
html,body{width:1200px;height:3130px;overflow:hidden}
body{font-family:"Open Sans",Arial,sans-serif;color:var(--grey);background:var(--white);position:relative}
.abs{position:absolute}
section,header,footer{position:absolute;left:0;width:1200px}

/* header */
.site-header{top:0;height:122px;background:var(--white)}
.nav a{position:absolute;top:62px;font-size:15px;font-weight:700;color:var(--dark);text-decoration:none;letter-spacing:.5px}
.nav a.active{color:var(--red)}
.brand{position:absolute;left:500px;top:22px;width:230px;text-align:center}
.brand-name{display:block;font-size:30px;font-weight:800;color:var(--red);line-height:1.1}
.brand-sub{display:block;font-size:12px;font-weight:700;color:var(--dark);letter-spacing:3px}
.phone{position:absolute;left:965px;top:60px;font-size:17px;font-weight:700;color:var(--red);display:flex;align-items:center;gap:8px}

/* hero */
.hero{top:122px;height:504px}
.hero-photo{position:absolute;inset:0;background:linear-gradient(180deg,#6b9ad4 0%,#9fbfe4 35%,#7a5a45 60%,#5a3f30 100%)}
.contact-panel{position:absolute;left:793px;top:69px;width:306px;height:383px;background:rgba(236,31,39,.85);padding:22px 28px}
.contact-panel h3{color:var(--white);text-align:center;font-size:16px;font-weight:700;letter-spacing:1px;margin-bottom:24px}
.field{height:40px;border:1px solid rgba(255,255,255,.7);margin-bottom:14px;color:var(--white);font-size:12px;padding:11px 12px;display:flex;justify-content:space-between;align-items:center}
.field.msg{height:70px;align-items:flex-start}
.send{position:absolute;right:28px;bottom:24px;background:var(--dark);color:var(--white);font-size:13px;font-weight:700;padding:8px 18px}
.dots{position:absolute;left:558px;top:470px;display:flex;gap:12px}
.dots span{width:12px;height:12px;border-radius:50%;background:rgba(255,255,255,.6)}
.dots span.on{background:var(--white)}

/* services */
.services{top:626px;height:452px}
.section-title{position:absolute;left:0;width:1200px;text-align:center;font-size:22px;font-weight:700;color:var(--dark);letter-spacing:1px}
.section-title::after{content:"";display:block;width:60px;height:3px;background:var(--red);margin:8px auto 0}
.experience{position:absolute;left:104px;top:85px;font-size:40px;font-weight:700;color:var(--dark);letter-spacing:1px}
.experience b{color:var(--red);font-size:70px;font-weight:800}
.intro{position:absolute;left:104px;top:178px;width:900px;font-size:20px;color:var(--mid);line-height:1.4}
.service-card{position:absolute;top:268px;width:400px;height:130px}
.num{position:absolute;left:0;top:0;width:122px;height:115px;color:var(--white);font-size:58px;font-weight:700;display:flex;align-items:center;justify-content:center}
.num.red{background:var(--red)}.num.dark{background:var(--dark)}
.service-card h4{position:absolute;left:167px;top:0;font-size:17px;font-weight:700;color:var(--dark)}
.service-card h4.red{color:var(--red)}
.service-card p{position:absolute;left:167px;top:28px;width:240px;font-size:14px;line-height:1.5;color:var(--mid)}
.finance-btn{position:absolute;left:1019px;top:393px;background:var(--red);color:var(--white);font-size:11px;font-weight:700;padding:7px 12px}

/* problems */
.problems{top:1078px;height:470px;background:linear-gradient(180deg,#3c3c3c,#2a2a2a)}
.problems .section-title{top:30px;color:var(--white);font-size:18px}
.problem{position:absolute;width:310px;height:100px}
.problem .icon{position:absolute;left:0;top:0;width:70px;height:70px;background:var(--red);display:flex;align-items:center;justify-content:center}
.problem h5{position:absolute;left:90px;top:4px;color:var(--white);font-size:16px;font-weight:700}
.problem p{position:absolute;left:90px;top:30px;width:220px;color:var(--light);font-size:13px;line-height:1.5}

/* projects */
.projects{top:1548px;height:434px}
.projects .section-title{top:70px;font-size:18px}
.project{position:absolute;top:140px;width:298px;height:280px}
.project .photo{position:absolute;left:0;top:0;width:100%;height:210px}
.project .label{position:absolute;left:0;top:120px;width:100%;height:158px;background:var(--red);clip-path:polygon(0 28%,100% 0,100% 100%,0 100%);padding:75px 0 0 18px;color:var(--white)}
.label h6{font-size:16px;font-weight:700;border-left:3px solid var(--white);padding-left:6px}
.label span{display:block;font-size:11px;margin-top:6px}

/* testimonials */
.clients{top:1982px;height:383px;background:linear-gradient(180deg,#2f3a4c 0%,#3a3a3a 40%,#222 100%)}
.clients .section-title{top:40px;color:var(--white);font-size:18px}
.avatar{position:absolute;left:565px;top:110px;width:70px;height:70px;border-radius:50%;background:#c9b9a6;border:3px solid var(--white)}
.client-name{position:absolute;left:0;width:1200px;top:190px;text-align:center;color:var(--white);font-size:18px;font-weight:700}
.quote{position:absolute;left:220px;top:232px;width:760px;text-align:center;color:var(--white);font-size:17px;line-height:1.5}
.circle-arrow{position:absolute;top:140px;width:50px;height:50px;border-radius:50%;border:2px solid var(--white);display:flex;align-items:center;justify-content:center}

/* partners */
.partners{top:2365px;height:226px}
.badge{position:absolute;top:92px;width:140px;height:40px;background:#d6d6d6}
.sq-arrow{position:absolute;top:98px;width:28px;height:28px;background:var(--dark);display:flex;align-items:center;justify-content:center}

/* subscribe */
.subscribe{top:2591px;height:94px;background:var(--charcoal)}
.sub-band{position:absolute;left:157px;top:0;width:904px;height:94px;background:var(--red);clip-path:polygon(6% 0,100% 0,94% 100%,0 100%)}
.sub-band h3{position:absolute;left:114px;top:30px;color:var(--white);font-size:24px;font-weight:700;letter-spacing:1px}
.sub-input{position:absolute;left:441px;top:28px;width:250px;height:40px;background:var(--white);font-size:12px;color:var(--light);padding:11px 14px}
.sub-btn{position:absolute;left:691px;top:28px;width:64px;height:40px;background:var(--dark);display:flex;align-items:center;justify-content:center}

/* footer */
.site-footer{top:2685px;height:445px;background:#333}
.fcol{position:absolute;top:78px}
.fcol h5{color:var(--white);font-size:14px;font-weight:700;margin-bottom:14px}
.fcol li{list-style:none;color:var(--light);font-size:12px;line-height:2}
.social li{display:flex;align-items:center;gap:12px;margin-bottom:12px}
.social i{width:30px;height:30px;border-radius:50%;background:#555;display:block}
.fcol p{color:var(--light);font-size:14px;line-height:1.6}
.bottom-bar{position:absolute;left:0;top:335px;width:1200px;height:110px;border-top:1px solid #444}
.bottom-bar p{position:absolute;left:96px;top:28px;color:var(--light);font-size:12px}
.live-chat{position:absolute;left:887px;top:62px;width:209px;height:48px;background:var(--red);color:var(--white);font-size:16px;font-weight:700;display:flex;align-items:center;justify-content:center;letter-spacing:1px}
</style>
</head>
<body>

<header class="site-header">
  <nav class="nav">
    <a href="#" class="active" style="left:225px">HOME</a>
    <a href="#" style="left:310px">ABOUT</a>
    <a href="#" style="left:405px">SERVICES ▾</a>
    <a href="#" style="left:740px">PROJECTS</a>
    <a href="#" style="left:840px">CONTACT US</a>
  </nav>
  <div class="brand"><span class="brand-name">Brightpeak Roofing</span><span class="brand-sub">ROOFING · SIDING · DOORS</span></div>
  <div class="phone"><svg width="16" height="16" viewBox="0 0 24 24"><path fill="#ec1f27" d="M6.6 10.8a15.1 15.1 0 0 0 6.6 6.6l2.2-2.2c.3-.3.7-.4 1-.2 1.1.4 2.3.6 3.6.6.6 0 1 .4 1 1V20c0 .6-.4 1-1 1A17 17 0 0 1 3 4c0-.6.4-1 1-1h3.5c.6 0 1 .4 1 1 0 1.3.2 2.5.6 3.6.1.3 0 .7-.2 1z"/></svg>-312-555-0148</div>
</header>

<section class="hero">
  <div class="hero-photo" role="img" aria-label="Photo of two roofers installing shingles on a roof under a blue sky"></div>
  <form class="contact-panel">
    <h3>GET IN TOUCH</h3>
    <div class="field">NAME <span>👤</span></div>
    <div class="field">EMAIL ID <span>✉</span></div>
    <div class="field">PHONE NO</div>
    <div class="field msg">MESSAGE</div>
    <div class="send">SEND</div>
  </form>
  <div class="dots"><span class="on"></span><span></span><span></span></div>
</section>

<section class="services">
  <h2 class="section-title" style="top:45px">SERVICES</h2>
  <div class="experience"><b>30</b> YEARS OF EXPERIENCE,</div>
  <p class="intro">If you're looking for reliable and trusted plumbing company we're at Your service, providing plumbing service</p>
  <div class="service-card" style="left:104px">
    <div class="num red">1</div>
    <h4>SINGLE ROOFS</h4>
    <p>Lorem Ipsum is simply dummy text of the printing and typesetting industry. Lorem Ipsum has been the industry's standard dummy text.</p>
  </div>
  <div class="service-card" style="left:602px">
    <div class="num dark">1</div>
    <h4 class="red">FLAT ROOFS</h4>
    <p>Lorem Ipsum is simply dummy text of the printing and typesetting industry. Lorem Ipsum has been the industry's standard dummy text.</p>
  </div>
  <div class="finance-btn">FINANCE</div>
</section>

<section class="problems">
  <h2 class="section-title">SOLVING ANY OF YOUR ROOFING PROBLEM</h2>
  <div class="problem" style="left:104px;top:104px"><div class="icon"><svg width="34" height="34" viewBox="0 0 24 24"><path fill="#fff" d="M12 3 2 12h3v8h5v-5h4v5h5v-8h3z"/></svg></div><h5>STRORM DAMAGE</h5><p>"Neque porro quisquam est qui dolorem ipsum quia dolor sit amet, consectetur, adipisci velit...</p></div>
  <div class="problem" style="left:435px;top:104px"><div class="icon"><svg width="34" height="34" viewBox="0 0 24 24"><rect x="3" y="4" width="18" height="16" fill="none" stroke="#fff" stroke-width="2"/><path fill="#fff" d="M5 18l5-6 4 4 2-2 3 4z"/></svg></div><h5>WINDOWS</h5><p>"Neque porro quisquam est qui dolorem ipsum quia dolor sit amet, consectetur, adipisci velit...</p></div>
  <div class="problem" style="left:772px;top:104px"><div class="icon"><svg width="34" height="34" viewBox="0 0 24 24"><path fill="#fff" d="M12 3 2 12h3v8h14v-8h3z"/></svg></div><h5>INSURANCE CLAIMS</h5><p>"Neque porro quisquam est qui dolorem ipsum quia dolor sit amet, consectetur, adipisci velit...</p></div>
  <div class="problem" style="left:104px;top:237px"><div class="icon"><svg width="34" height="34" viewBox="0 0 24 24"><path fill="none" stroke="#fff" stroke-width="2" d="M4 6h16M6 6v12M18 6v12"/></svg></div><h5>GUTTERS</h5><p>"Neque porro quisquam est qui dolorem ipsum quia dolor sit amet, consectetur, adipisci velit...</p></div>
  <div class="problem" style="left:435px;top:237px"><div class="icon"><svg width="34" height="34" viewBox="0 0 24 24"><path fill="none" stroke="#fff" stroke-width="2" d="M5 19 15 9M14 4l6 6-3 3-6-6z"/></svg></div><h5>CARPENTRY</h5><p>"Neque porro quisquam est qui dolorem ipsum quia dolor sit amet, consectetur, adipisci velit...</p></div>
  <div class="problem" style="left:772px;top:237px"><div class="icon"><svg width="34" height="34" viewBox="0 0 24 24"><rect x="5" y="3" width="14" height="18" fill="none" stroke="#fff" stroke-width="2"/><path stroke="#fff" stroke-width="2" d="M5 10h14"/></svg></div><h5>KITCHENS&amp;BATHS</h5><p>"Neque porro quisquam est qui dolorem ipsum quia dolor sit amet, consectetur, adipisci velit...</p></div>
</section>

<section class="projects">
  <h2 class="section-title">PROJECT</h2>
  <div class="project" style="left:104px"><div class="photo" role="img" aria-label="Photo of a roofer working on a red tiled roof" style="background:linear-gradient(160deg,#9cc3e8,#c0473a 65%)"></div><div class="label"><h6>ROOFING REPAIR</h6><span>AUG,2016 TO OCT,2016</span></div></div>
  <div class="project" style="left:442px"><div class="photo" role="img" aria-label="Photo of a worker in a hard hat laying roof tiles" style="background:linear-gradient(160deg,#e5e9ee,#b5543f 70%)"></div><div class="label"><h6>ROOFING REPAIR</h6><span>JUNE 2016 TO JUL,2016</span></div></div>
  <div class="project" style="left:800px"><div class="photo" role="img" aria-label="Photo of a roofer holding a shingle sheet" style="background:linear-gradient(160deg,#8bb4dc,#5b7a4a 70%)"></div><div class="label"><h6>ROOFING REPAIR</h6><span>START OCT</span></div></div>
</section>

<section class="clients">
  <h2 class="section-title">HAPPY CLIENTS</h2>
  <div class="avatar" role="img" aria-label="Client portrait"></div>
  <div class="client-name">MARCUS ELLERY</div>
  <p class="quote">Lorem Ipsum is simply dummy text of the printing and typesetting industry. Lorem Ipsum has been the industry's standard dummy text ever since the 1500s. Lorem Ipsum is simply dummy text of the printing and typesetting industry. Lorem Ipsum has been the industry's standard dummy text ever since the 1500s.</p>
  <div class="circle-arrow" style="left:96px"><svg width="18" height="18" viewBox="0 0 24 24"><path fill="#fff" d="M16 4 7 12l9 8z"/></svg></div>
  <div class="circle-arrow" style="left:1054px"><svg width="18" height="18" viewBox="0 0 24 24"><path fill="#fff" d="m8 4 9 8-9 8z"/></svg></div>
</section>

<section class="partners">
  <div class="sq-arrow" style="left:40px"><svg width="12" height="12" viewBox="0 0 24 24"><path fill="#fff" d="M16 4 7 12l9 8z"/></svg></div>
  <div class="badge" style="left:130px"></div>
  <div class="badge" style="left:290px"></div>
  <div class="badge" style="left:450px"></div>
  <div class="badge" style="left:610px"></div>
  <div class="badge" style="left:770px"></div>
  <div class="badge" style="left:930px"></div>
  <div class="sq-arrow" style="left:1120px"><svg width="12" height="12" viewBox="0 0 24 24"><path fill="#fff" d="m8 4 9 8-9 8z"/></svg></div>
</section>

<section class="subscribe">
  <div class="sub-band"><h3>SUBSCRIBE OUR NEWS</h3><div class="sub-input">EMAIL</div><div class="sub-btn"><svg width="18" height="18" viewBox="0 0 24 24"><path fill="#fff" d="M2 12 22 3l-6 18-4-7z"/></svg></div></div>
</section>

<footer class="site-footer">
  <div class="fcol" style="left:104px"><h5>MENU ▾</h5><ul><li>HOME</li><li>ABOUT US</li><li>SERVICES</li><li>PROJECT</li><li>NEWS</li><li>HAPPY CLIENTS</li><li>CONTACT US</li></ul></div>
  <div class="fcol social" style="left:296px"><h5>FIND US</h5><ul><li><i></i>FRIENDLINE</li><li><i></i>CHIRPER</li><li><i></i>SNAPFRAME</li><li><i></i>EMAIL</li></ul></div>
  <div class="fcol" style="left:522px;width:260px"><h5>ABOUT US</h5><p>Lorem Ipsum is simply dummy text of the printing and typesetting industry. Lorem Ipsum has been the industry's standard dummy text ever since the 1500s.</p></div>
  <div class="fcol" style="left:845px;width:270px"><h5>CONTACT US</h5><p>BRIGHTPEAK ROOFING &amp; CONSTRUCTION COMPANY, INC.<br>Residential/Commercial/Industrial Roofing License #100.000000 100.000001</p><p style="margin-top:22px">Illinois 312-555-0148<br>Indiana 219-555-0172</p></div>
  <div class="bottom-bar"><p>Site Map &nbsp;|&nbsp; Privacy &nbsp;|&nbsp; Terms Use &nbsp;|&nbsp; © Brightpeak Roofing Construction Company. All right reserved</p><div class="live-chat">LIVE CHAT</div></div>
</footer>

</body>
</html>
```